Business cards and letterhead
Business cards and letterhead - Pharmacy/Pharmaceuticals
Creative Brief
Professional
Owen Lilcroft
Partner
4178 Heron Lake Road Suite 410 Fernbrook, CO 80931
owen@torvalepz.com
torvalepz.com

```html
<!DOCTYPE html>
<html lang="en">
<head>
<meta charset="utf-8">
<title>Torvale Medical Solutions – Business Card</title>
<link href="https://fonts.googleapis.com/css2?family=PT+Sans:wght@400;700&display=swap" rel="stylesheet">
<style>
  :root {
    --stage: #e9ecf0;
    --blue-deep: #0d5fb8;
    --blue-main: #1877d2;
    --blue-light: #4fa3ec;
    --white: #ffffff;
    --ink-soft: #dbe9f8;
    --shadow: rgba(10, 30, 60, 0.22);
  }
  * { box-sizing: border-box; margin: 0; padding: 0; }
  html, body { width: 1200px; height: 901px; overflow: hidden; }
  body {
    background: var(--stage);
    font-family: "PT Sans", sans-serif;
    position: relative;
  }
  .card {
    position: absolute;
    width: 520px;
    height: 297px;
    border-radius: 18px;
    overflow: hidden;
    box-shadow: 0 10px 28px var(--shadow);
  }
  .card--back {
    left: 50px; top: 302px;
    background: linear-gradient(160deg, var(--blue-light) 0%, var(--blue-main) 45%, var(--blue-deep) 100%);
    display: flex; align-items: center; justify-content: center;
  }
  .back-mark { display: flex; align-items: center; gap: 12px; }
  .back-mark .dot {
    width: 26px; height: 26px; border-radius: 50%;
    background: var(--white);
  }
  .back-mark .brand-name { font-size: 34px; font-weight: 700; color: var(--white); }
  .card--front {
    left: 630px; top: 302px;
    background: var(--white);
  }
  .front-top {
    height: 140px;
    display: flex; flex-direction: column; align-items: center; justify-content: center;
  }
  .brand { display: flex; align-items: center; gap: 12px; }
  .brand .dot {
    width: 30px; height: 30px; border-radius: 50%;
    background: var(--blue-main);
  }
  .brand .brand-name {
    font-size: 40px; font-weight: 700; color: var(--blue-main); line-height: 1;
  }
  .tagline {
    margin-top: 4px; margin-left: 86px;
    font-size: 9px; font-weight: 700; letter-spacing: 1.5px; color: var(--blue-main);
  }
  .rule { height: 3px; background: var(--blue-main); margin-top: 6px; }
  .front-band {
    position: absolute; left: 0; right: 0; bottom: 0; top: 150px;
    background: linear-gradient(180deg, var(--blue-light) 0%, var(--blue-main) 55%, var(--blue-deep) 100%);
    display: flex; padding: 16px 0 0 0;
  }
  .person {
    width: 258px; text-align: right; padding-right: 18px; color: var(--white);
  }
  .person .name { font-size: 17px; font-weight: 700; }
  .person .role { font-size: 11px; color: var(--ink-soft); margin-bottom: 10px; }
  .person .address { font-size: 12px; line-height: 1.3; }
  .divider { width: 1px; background: var(--ink-soft); margin: 2px 0 18px; }
  .contacts {
    list-style: none; padding-left: 12px; color: var(--white); font-size: 12px; line-height: 1.45;
  }
  .contacts li { display: flex; align-items: center; gap: 8px; white-space: nowrap; }
  .contacts svg { width: 10px; height: 10px; fill: var(--white); flex: none; }
</style>
</head>
<body>
  <section class="card card--back" aria-label="Card back">
    <div class="back-mark">
      <span class="dot"></span>
      <span class="brand-name">Torvale</span>
    </div>
  </section>

  <section class="card card--front" aria-label="Card front">
    <div class="front-top">
      <div class="brand">
        <span class="dot"></span>
        <span class="brand-name">Torvale</span>
      </div>
      <div class="tagline">MEDICAL SOLUTIONS</div>
    </div>
    <div class="rule"></div>
    <div class="front-band">
      <div class="person">
        <div class="name">Owen Lilcroft</div>
        <div class="role">Partner</div>
        <div class="address">4178 Heron Lake Road<br>Suite 410<br>Fernbrook, CO 80931</div>
      </div>
      <div class="divider"></div>
      <ul class="contacts">
        <li><svg viewBox="0 0 10 10"><path d="M2 0h2l1 2.5-1.3 1a5 5 0 0 0 2.8 2.8l1-1.3L10 6v2c0 1-1 2-2 2A8 8 0 0 1 0 2c0-1 1-2 2-2z"/></svg>5550142233</li>
        <li><svg viewBox="0 0 10 10"><rect x="2.5" y="0" width="5" height="10" rx="1"/></svg>5550187764</li>
        <li><svg viewBox="0 0 10 10"><rect x="0" y="3" width="10" height="6" rx="1"/><rect x="2" y="0" width="6" height="3"/></svg>5550129905</li>
        <li><svg viewBox="0 0 10 10"><path d="M2 0h2l1 2.5-1.3 1a5 5 0 0 0 2.8 2.8l1-1.3L10 6v2c0 1-1 2-2 2A8 8 0 0 1 0 2c0-1 1-2 2-2z"/></svg>5550163341</li>
        <li><svg viewBox="0 0 10 10"><rect x="0" y="1.5" width="10" height="7" rx="1"/></svg>owen@torvalepz.com</li>
        <li><svg viewBox="0 0 10 10"><circle cx="5" cy="5" r="5"/></svg>torvalepz.com</li>
      </ul>
    </div>
  </section>
</body>
</html>
```